Website design needed for Renewable utilities company based in New Zealand.

Website design needed for Lanternvale Holdings based in New Zealand.

Please see attached logo.

We sell solar panels, vertical axis wind turbines, atmospheric water generators and other related equipment for those who don't have access or don't want to depend on the government, city councils for their utilities (power and water).

We like metallic texture, dark grey and purple, red or blue colours. The design should go well with the attached logo.

Target Market(s)

The Eco conscious

Industry/Entity Type

Government

Logo Text

Lanternvale Summit

Requirements
Must have
• Must Have:
- Metallic finish is a must.
- Design should fit around the attached logo well.
Nice to have
• Sharpe design prefred rather than rounded edges

```html
<!DOCTYPE html>
<html lang="en">
<head>
<meta charset="utf-8">
<title>Lanternvale Summit — Renewable Utilities</title>
<link rel="stylesheet" href="https://fonts.googleapis.com/css2?family=Comfortaa:wght@400;700&family=Arimo:wght@400;700&family=Roboto+Condensed:wght@400;700&display=swap">
<style>
:root{
  --page:#e9eaec;
  --white:#ffffff;
  --ink:#4a4d52;
  --muted:#7b7f86;
  --blue:#2a66ae;
  --navy:#1d2f5a;
  --navy-deep:#16244a;
  --red:#d8262a;
  --line:#d5d7db;
  --metal-1:#fbfbfc;
  --metal-2:#c9ccd1;
  --metal-3:#9a9ea5;
}
*{box-sizing:border-box;margin:0;padding:0}
html,body{width:898px;height:1200px;overflow:hidden}
body{position:relative;background:var(--page);font-family:"Arimo",Arial,sans-serif;color:var(--ink);font-size:12px;line-height:1.45}

.site-header{position:absolute;left:0;top:0;width:898px;height:118px;background:linear-gradient(#fff,#f1f2f4)}
.brand{position:absolute;left:24px;top:30px;display:flex;align-items:center;gap:10px}
.brand-dot{width:26px;height:26px;border-radius:50%;background:var(--blue)}
.brand-name{font-family:"Comfortaa",sans-serif;font-weight:700;font-size:20px;color:var(--navy)}
.social-top{position:absolute;right:30px;top:14px;display:flex;gap:6px}
.social-top span{width:18px;height:18px;background:var(--blue)}
.social-top span:nth-child(3){background:var(--red)}
.phone{position:absolute;right:30px;top:42px;font-family:"Roboto Condensed",sans-serif;font-weight:700;font-size:26px;color:var(--red)}

.main-nav{position:absolute;left:96px;top:86px;width:706px;height:28px;display:flex;background:linear-gradient(#fdfdfd,#dcdee2);border:1px solid var(--line)}
.main-nav a{flex:0 0 auto;padding:0 22px;line-height:26px;font-size:11px;text-transform:uppercase;color:var(--muted);text-decoration:none;border-right:1px solid var(--line)}
.main-nav a.active{background:linear-gradient(#4f86c9,var(--blue));color:#fff}

.hero{position:absolute;left:0;top:118px;width:898px;height:340px;background:linear-gradient(100deg,var(--metal-1) 0%,#e3e5e8 45%,var(--metal-2) 75%,#b9bcc2 100%);border-bottom:1px solid var(--metal-3)}
.hero-title{position:absolute;left:108px;top:120px;font-family:"Comfortaa",sans-serif;font-size:50px;color:#2d2f33;letter-spacing:.5px}
.hero-text{position:absolute;left:108px;top:206px;width:260px;font-size:12px;color:#3c3f44}
.hero-media{position:absolute;left:440px;top:40px;width:380px;height:280px;background:linear-gradient(150deg,#3b4f82,#1f2d57 60%,#7d8aa6);transform:skewY(-6deg)}
.pager{position:absolute;left:0;top:478px;width:898px;display:flex;justify-content:center;gap:8px}
.pager span{width:34px;height:3px;background:#c4c7cc}
.pager span.on{background:#8a8e95}

.content{position:absolute;left:84px;top:500px;width:730px;height:530px;background:var(--white)}
.features{position:absolute;left:12px;top:20px;display:flex;gap:16px}
.feature{width:224px;height:330px;border:1px solid var(--line);background:linear-gradient(#fff,#f4f5f7);padding:14px}
.feature h3{font-family:"Roboto Condensed",sans-serif;font-weight:700;font-size:15px;color:var(--blue);margin-bottom:12px;white-space:nowrap}
.feature-media{height:96px;margin-bottom:10px}
.m-solar{background:linear-gradient(#8fb8e6,#2d4f8a)}
.m-wind{background:linear-gradient(#d7e3f1,#a8c0dc)}
.m-water{background:linear-gradient(#e9eef3,#9aa7b5)}
.feature p{font-size:11px;color:var(--muted);height:56px}
.btn{display:inline-block;margin-top:10px;padding:4px 12px;font-size:10px;color:#fff;background:linear-gradient(#5a5e65,#34373c);text-decoration:none}

.welcome{position:absolute;left:12px;top:370px;width:706px}
.welcome h2{font-family:"Roboto Condensed",sans-serif;font-weight:700;font-size:17px;color:var(--blue);margin-bottom:8px}
.welcome p{font-size:11px;color:var(--muted);margin-bottom:10px}

.site-footer{position:absolute;left:0;top:1040px;width:898px;height:160px;background:linear-gradient(var(--navy),var(--navy-deep));color:#c9d2e6;font-size:10px}
.newsletter{position:absolute;left:96px;top:16px}
.newsletter h4,.news h4{font-size:12px;color:#fff;margin-bottom:6px}
.subscribe{display:flex}
.subscribe span{width:190px;height:20px;background:#fff;color:#999;padding:3px 6px}
.subscribe b{width:46px;height:20px;background:var(--blue);color:#fff;text-align:center;line-height:20px;font-weight:400}
.news{position:absolute;left:392px;top:14px;width:422px}
.news-items{display:flex;gap:24px}
.news-item{width:196px;line-height:1.3}
.news-item strong{color:#fff;display:block}
.footer-bottom{position:absolute;left:96px;top:112px;width:718px;display:flex;justify-content:space-between;align-items:center}
.footer-links a{color:#c9d2e6;text-decoration:none;margin-right:6px}
.social-bottom{display:flex;gap:6px}
.social-bottom span{width:20px;height:20px;border-radius:50%;background:#8a96ad}
</style>
</head>
<body>
<header class="site-header">
  <div class="brand"><span class="brand-dot"></span><span class="brand-name">Lanternvale Summit</span></div>
  <div class="social-top"><span></span><span></span><span></span></div>
  <div class="phone">800-555-0142</div>
  <nav class="main-nav">
    <a class="active" href="#">Home</a><a href="#">About Us</a><a href="#">Services</a><a href="#">Products</a><a href="#">News</a><a href="#">Contact Us</a>
  </nav>
</header>

<section class="hero">
  <h1 class="hero-title">Solar Panel</h1>
  <p class="hero-text">Clean power and water for homes that stand on their own, far from the grid and built to last through every season.</p>
  <div class="hero-media" role="img" aria-label="Photo of a tilted solar panel array"></div>
</section>
<div class="pager"><span></span><span class="on"></span><span></span></div>

<main class="content">
  <div class="features">
    <article class="feature">
      <h3>Solar Panels</h3>
      <div class="feature-media m-solar" role="img" aria-label="Photo of solar panels under a blue sky"></div>
      <p>High-yield panels that turn daylight into steady, reliable household power.</p>
      <a class="btn" href="#">Read more ›</a>
    </article>
    <article class="feature">
      <h3>Vertical Axis Wind Turbines</h3>
      <div class="feature-media m-wind" role="img" aria-label="Photo of a vertical axis wind turbine"></div>
      <p>Quiet turbines that catch wind from any direction, day and night.</p>
      <a class="btn" href="#">Read more ›</a>
    </article>
    <article class="feature">
      <h3>Atmospheric Water Generators</h3>
      <div class="feature-media m-water" role="img" aria-label="Photo of an atmospheric water generator unit"></div>
      <p>Units that draw clean drinking water straight from the humid air.</p>
      <a class="btn" href="#">Read more ›</a>
    </article>
  </div>
  <section class="welcome">
    <h2>Welcome to Lanternvale Summit</h2>
    <p>We supply equipment for people who would rather make their own power and water than rely on councils or central networks. Our solar panels, wind turbines and water generators are chosen for tough conditions and long service, and every system comes with advice on sizing, installation and care so you can live comfortably off the grid.</p>
    <p>From remote farms to coastal baches, our team helps households across New Zealand plan a setup that fits their site, their budget and the way they live. Talk to us about a complete kit or a single part to add to the system you already run.</p>
  </section>
</main>

<footer class="site-footer">
  <div class="newsletter">
    <h4>Subscribe Our Newsletter!</h4>
    <div class="subscribe"><span>Your email</span><b>Go</b></div>
  </div>
  <div class="news">
    <h4>Latest News</h4>
    <div class="news-items">
      <div class="news-item"><strong>New turbine range</strong>12 May 2024<br>Our quieter vertical turbines arrive in stores next month. Read more</div>
      <div class="news-item"><strong>Winter solar tips</strong>03 May 2024<br>How to keep panels clear and working through the short days. Read more</div>
    </div>
  </div>
  <div class="footer-bottom">
    <div>
      <div class="footer-links"><a href="#">Home</a>| <a href="#">About Us</a>| <a href="#">Services</a>| <a href="#">Products</a>| <a href="#">News</a>| <a href="#">Contact</a></div>
      <div>Copyright © 2024 Lanternvale Summit. All rights reserved.</div>
    </div>
    <div class="social-bottom"><span></span><span></span><span></span></div>
  </div>
</footer>
</body>
</html>
```